Passionate Homecare Agency Needs an "Employee News" Webpage Design

We are a homecare agency with more than 300 employees who provide personal care and assistance with the activities of daily living in clients’ homes. Our company slogan is “Someone you can depend on… Without question.” We strive to provide our clients with the highest quality, compassionate care possible, and we want our employees to feel inspired to do just that.

We are looking for an employee web page design to add to our existing website that makes our field employees feel connected to the company, is fun and energetic, and provides our caregivers with helpful information, employee news, and recognition. We want this to be a hub for communication and celebration, and also showcase our appreciation for all that they do!

We look forward to your designs! The sky's the limit!
Updates

Reason: Looking for a few more designs that fit our descriptions before making a final decision.

Target Market(s)

Our Employees

Industry/Entity Type

Home Health Care

Number of Pages Required

1 page

Colors

Designer to choose colors to be used in the design.

Requirements
Must have
• We would like to have sections like:
• -Employee of the Month/Week
• -Caregiver Tips and Tricks
• -Birthdays and Anniversaries
• -New Employees
• -Area to add links to our social media (Facebook, Instagram, Twitter)
• -etc!
Nice to have
• Bright colors and fun themes.

```html
<!DOCTYPE html>
<html lang="en">
<head>
<meta charset="utf-8">
<title>Employee News</title>
<link rel="stylesheet" href="https://fonts.googleapis.com/css2?family=Raleway:wght@400;500;700;800&family=Open+Sans:wght@400;600&family=Source+Sans+3:wght@400;600&display=swap">
<style>
:root{
  --band:#e5edf0;
  --white:#ffffff;
  --ink:#1f2428;
  --text:#45494d;
  --blue:#1a73e8;
  --icon-bg:#e6eef1;
  --divider:#c3ccd1;
  --dot:#b9c8cf;
  --social:#a4adb3;
}
*{margin:0;padding:0;box-sizing:border-box}
html,body{width:1200px;height:1200px;overflow:hidden}
body{position:relative;background:var(--white);font-family:"Open Sans",sans-serif;color:var(--text)}
.abs{position:absolute}

.spotlight{left:0;top:0;width:1200px;height:224px;background:var(--band)}
.quote-mark{left:170px;top:27px}
.quote-text{left:244px;top:24px;width:392px;font-family:"Source Sans 3",sans-serif;font-size:11.6px;line-height:18px;color:#3b4045}
.quote-by{left:244px;top:131px;font-family:"Source Sans 3",sans-serif;font-size:10.5px;color:#50565b}
.quote-name{left:244px;top:146px;font-family:"Source Sans 3",sans-serif;font-size:10.5px;font-weight:600;color:var(--ink);letter-spacing:.2px}
.quote-divider{left:661px;top:0;width:1px;height:154px;background:var(--divider)}
.avatar{top:21px;width:100px;height:100px;border-radius:50%;background:radial-gradient(circle at 50% 40%,#c9b2a2,#6f7378 75%)}
.slider-dots{left:834px;top:134px;display:flex;gap:8px}
.slider-dots span{width:8px;height:8px;border-radius:50%;background:var(--dot)}
.slider-dots span.active{background:var(--blue)}

.section-title{font-family:"Raleway",sans-serif;font-weight:800;font-size:22px;color:var(--ink);letter-spacing:.5px;line-height:1}
.section-sub{font-family:"Raleway",sans-serif;font-weight:500;font-size:12px;color:var(--ink);letter-spacing:1.3px}

.tip-icon{width:51px;height:51px;background:var(--icon-bg);display:flex;align-items:center;justify-content:center}
.tip-icon svg{width:32px;height:32px;fill:none;stroke:#2b3035;stroke-width:1.2;stroke-linejoin:round;stroke-linecap:round}
.tip-title{font-family:"Raleway",sans-serif;font-size:15.5px;color:var(--ink);letter-spacing:.3px;white-space:nowrap}
.tip-body{width:195px;font-size:11px;line-height:18px;color:var(--text)}

.btn-more{left:540px;top:618px;width:120px;height:28px;border-radius:14px;background:var(--blue);color:var(--white);font-size:10px;font-weight:600;letter-spacing:.8px;display:flex;align-items:center;justify-content:center}

.celebrations{left:0;top:720px;width:1200px;height:480px;background:var(--band)}
.card{top:861px;width:198px;height:297px;background:var(--white)}
.card.featured{box-shadow:0 4px 28px rgba(80,140,170,.28)}
.card-photo{width:198px;height:206px}
.card-name{position:absolute;left:22px;top:224px;font-family:"Source Sans 3",sans-serif;font-size:10.5px;color:var(--ink);letter-spacing:.1px}
.card-role{position:absolute;left:22px;top:240px;font-size:10px;color:var(--blue);letter-spacing:.2px}
.card-social{position:absolute;left:22px;top:265px;display:flex;gap:11px}
.card-social span{width:9px;height:9px;border-radius:50%;background:var(--social)}
</style>
</head>
<body>

<section class="abs spotlight">
  <svg class="abs quote-mark" width="44" height="36" viewBox="0 0 44 36" aria-hidden="true">
    <path fill="#262a2e" d="M0 36V20C0 8 6 1 17 0v7c-5 1-8 4-8 10h8v19zM26 36V20C26 8 32 1 43 0v7c-5 1-8 4-8 10h8v19z"/>
  </svg>
  <p class="abs quote-text">Every morning she arrives with a smile, a warm cup of tea and a plan for the day. Her clients say she feels like family, and her teammates say she is the first to help when a shift runs long. This month we thank her for the patience, kindness and care she brings into every home. Someone you can depend on… without question. ....</p>
  <div class="abs quote-by">Employee of the Month</div>
  <div class="abs quote-name">MARISOL VANTERPOOL</div>
  <div class="abs quote-divider"></div>
  <div class="abs avatar" style="left:684px" role="img" aria-label="Portrait of the employee of the month"></div>
  <div class="abs avatar" style="left:805px" role="img" aria-label="Portrait of the employee of the week"></div>
  <div class="abs avatar" style="left:927px" role="img" aria-label="Portrait of a recognised caregiver"></div>
  <div class="abs slider-dots"><span class="active"></span><span></span><span></span></div>
</section>

<section class="tips">
  <h2 class="abs section-title" style="left:170px;top:298px">CAREGIVER TIPS</h2>
  <div class="abs section-sub" style="left:170px;top:322px">TIPS AND TRICKS FOR EVERY VISIT</div>

  <div class="abs tip-icon" style="left:171px;top:381px"><svg viewBox="0 0 28 28"><rect x="4" y="6" width="5" height="16"/><rect x="10" y="6" width="5" height="16"/><path d="M16 7l4-1 4 15-4 1z"/><path d="M5 10h3M11 10h3M5 18h3M11 18h3"/></svg></div>
  <div class="abs tip-title" style="left:244px;top:377px">Keep a daily care log</div>
  <p class="abs tip-body" style="left:244px;top:403px">Note meals, moods and medicine times so the next caregiver picks up right where you left off.</p>

  <div class="abs tip-icon" style="left:464px;top:381px"><svg viewBox="0 0 28 28"><path d="M2 10l6-5 5 3 4-3 9 6-3 3"/><path d="M2 10l3 4 8 8c1 1 2 1 3 0l8-8"/><path d="M10 15l3 3M13 13l3 3M16 11l3 3"/></svg></div>
  <div class="abs tip-title" style="left:538px;top:377px">Build trust with clients</div>
  <p class="abs tip-body" style="left:538px;top:403px">Explain each step before you help, ask how they like things done and let them lead when they can.</p>

  <div class="abs tip-icon" style="left:757px;top:381px"><svg viewBox="0 0 28 28"><circle cx="14" cy="5" r="2"/><path d="M11 11h6v-2a3 3 0 0 0-6 0z"/><circle cx="6" cy="16" r="2"/><path d="M3 22h6v-2a3 3 0 0 0-6 0z"/><circle cx="22" cy="16" r="2"/><path d="M19 22h6v-2a3 3 0 0 0-6 0z"/><path d="M14 12v3M9 17l5-2 5 2"/></svg></div>
  <div class="abs tip-title" style="left:830px;top:377px">Keep families in the loop</div>
  <p class="abs tip-body" style="left:830px;top:403px">A short friendly update at the end of a visit helps loved ones feel close and reassured.</p>

  <div class="abs tip-icon" style="left:171px;top:498px"><svg viewBox="0 0 28 28"><path d="M3 5h22M4 5v14h20V5M14 19v4M12 24h4"/><circle cx="13" cy="12" r="4"/><path d="M13 12h4M13 12V8"/></svg></div>
  <div class="abs tip-title" style="left:248px;top:494px">Plan safe transfers</div>
  <p class="abs tip-body" style="left:244px;top:520px">Clear the path, lock the wheels and bend your knees. Your back will thank you at the end of the week.</p>

  <div class="abs tip-icon" style="left:464px;top:498px"><svg viewBox="0 0 28 28"><rect x="9" y="5" width="9" height="17" rx="1"/><rect x="11" y="7" width="5" height="3"/><path d="M11 13h1M13 13h1M15 13h1M11 16h1M13 16h1M15 16h1M11 19h1M13 19h1M15 19h1"/><path d="M6 14v10h16V14M12 2v3"/></svg></div>
  <div class="abs tip-title" style="left:538px;top:494px">Call the office anytime</div>
  <p class="abs tip-body" style="left:538px;top:520px">Our on-call team is ready day and night. No question is too small when a client needs help.</p>

  <div class="abs tip-icon" style="left:757px;top:498px"><svg viewBox="0 0 28 28"><rect x="3" y="8" width="22" height="15" rx="1"/><path d="M10 8V5h8v3M3 14h22"/><rect x="12" y="12" width="4" height="4"/></svg></div>
  <div class="abs tip-title" style="left:830px;top:494px">Pack your visit kit</div>
  <p class="abs tip-body" style="left:830px;top:520px">Gloves, hand cleaner, a pen and a spare mask. A ready bag makes every visit calm and smooth.</p>

  <div class="abs btn-more">MORE TIPS</div>
</section>

<section class="abs celebrations"></section>
<h2 class="abs section-title" style="left:173px;top:795px">CELEBRATIONS</h2>
<div class="abs section-sub" style="left:173px;top:819px">BIRTHDAYS, ANNIVERSARIES AND NEW FACES</div>

<article class="abs card" style="left:173px">
  <div class="card-photo" role="img" aria-label="Photo of a caregiver celebrating a birthday" style="background:linear-gradient(180deg,#a9cfe0,#7fb3cc)"></div>
  <div class="card-name">ODALYS PRENTICE</div>
  <div class="card-role">Happy Birthday · March 4</div>
  <div class="card-social"><span></span><span></span><span></span><span></span></div>
</article>
<article class="abs card featured" style="left:393px">
  <div class="card-photo" role="img" aria-label="Photo of a caregiver marking a work anniversary" style="background:linear-gradient(180deg,#d6dadd,#eef0f1)"></div>
  <div class="card-name">RENATA CALLOWAY</div>
  <div class="card-role">10 Year Anniversary</div>
  <div class="card-social"><span></span><span></span><span></span><span></span></div>
</article>
<article class="abs card" style="left:612px">
  <div class="card-photo" role="img" aria-label="Photo of a new caregiver in blue scrubs" style="background:linear-gradient(180deg,#4b4f5a,#4f74a8)"></div>
  <div class="card-name">JOLENE MARSDEN</div>
  <div class="card-role">New Employee · Welcome!</div>
  <div class="card-social"><span></span><span></span><span></span><span></span></div>
</article>
<article class="abs card" style="left:832px">
  <div class="card-photo" role="img" aria-label="Photo of a caregiver marking a work anniversary" style="background:linear-gradient(180deg,#6e5a4c,#c9c6c2)"></div>
  <div class="card-name">DESMOND OKAFOR-LYLE</div>
  <div class="card-role">5 Year Anniversary</div>
  <div class="card-social"><span></span><span></span><span></span><span></span></div>
</article>

</body>
</html>
```